Beautiful Quotes For Social Media Posts

We are looking for 5 beautifully designed quotes for our social media account.

Inspiration of styles we like in both style and color along with a few of our favorite fonts (you are NOT limited to these fonts this is just to give you an idea):
https://morrowstudio.example.net/s/k7p2q9x4m1t8v3n6b5c0z2w8y4j1

*These fonts are property of Morrow Studio. You do not have permission/rights to use them outside of this assignment*

Quotes to use (5):
“Only those who dare to fail greatly can ever achieve greatly.” –Walter J. Simmons
“Don’t go through life, grow through life.” – Neil Ashcombe
“Follow your bliss and the universe will open doors where there were only walls.” – Martin Oakley
“If you don’t like the road you’re walking, start paving another one.” – Greta Vance
“Life is like riding a bicycle. To keep your balance, you must keep moving.” —Oskar Feldmann

File Specifics:
- JPG
- 10x10 in size (square)
- Please include @MorrowStudio in the bottom right left or center of each design

Brand Details:
Soft but rich pastel and bright colors.
Hand Drawn florals, doodles and art
Handwritten looking fonts
Artsy, Creative, Girl and Inspiring

```html
<!DOCTYPE html>
<html lang="en">
<head>
<meta charset="utf-8">
<title>Quote Posts – Morrow Studio</title>
<link rel="stylesheet" href="https://fonts.googleapis.com/css2?family=Caveat+Brush&family=Caveat:wght@500;700&family=Kaushan+Script&family=Amatic+SC:wght@700&family=Dancing+Script:wght@500&display=swap">
<style>
  :root {
    --page: #e6e0d6;
    --rose-light: #b0646e;
    --rose-dark: #874150;
    --blush: #f3e4e3;
    --berry: #8e1d45;
    --ring: #dd5680;
    --faint-petal: #e6b9c0;
    --deep-teal: #062829;
    --teal: #0b4c54;
    --white: #ffffff;
  }
  * { margin: 0; padding: 0; box-sizing: border-box; }
  html, body { width: 1200px; height: 412px; overflow: hidden; background: var(--page); }
  .post-row { position: relative; width: 1200px; height: 412px; }
  .post {
    position: absolute; top: 46px; width: 314px; height: 314px; overflow: hidden;
    box-shadow: 0 3px 10px rgba(0,0,0,.18);
  }
  .post svg { position: absolute; inset: 0; width: 314px; height: 314px; }
  .post-text { position: absolute; left: 0; width: 100%; text-align: center; white-space: nowrap; }
  .handle { position: absolute; left: 0; width: 100%; text-align: center; font-family: "Caveat", cursive; font-weight: 700; font-size: 17px; }

  /* Card 1 – rose hexagon */
  .post--rose { left: 69px; background: linear-gradient(160deg, var(--rose-light), var(--rose-dark) 55%, var(--rose-light)); color: var(--white); }
  .post--rose .quote { font-family: "Caveat Brush", cursive; font-size: 20px; line-height: 21px; top: 118px; }
  .post--rose .quote .small { font-size: 17px; }
  .post--rose .author { font-family: "Caveat", cursive; font-weight: 700; font-size: 21px; top: 206px; }
  .post--rose .closing-mark { font-family: Georgia, serif; font-weight: 700; font-size: 30px; top: 186px; line-height: 30px; }
  .post--rose .handle { top: 287px; }

  /* Card 2 – blush ring */
  .post--blush { left: 445px; background: var(--blush); color: var(--berry); }
  .post--blush .headline { font-family: "Kaushan Script", cursive; font-size: 33px; line-height: 36px; top: 62px; }
  .post--blush .caps { font-family: "Amatic SC", sans-serif; font-weight: 700; font-size: 34px; line-height: 28px; top: 134px; }
  .post--blush .author { font-family: "Caveat", cursive; font-weight: 700; font-size: 20px; top: 197px; }
  .post--blush .author::before, .post--blush .author::after {
    content: ""; display: inline-block; width: 28px; height: 2px; background: var(--berry); vertical-align: middle; margin: 0 6px;
  }
  .post--blush .quote-mark { position: absolute; font-family: Georgia, serif; font-weight: 700; font-size: 96px; line-height: 1; color: var(--berry); }
  .post--blush .quote-mark--open { left: 30px; top: 44px; }
  .post--blush .quote-mark--close { left: 206px; top: 232px; }
  .post--blush .handle { top: 288px; color: var(--ring); }

  /* Card 3 – teal frame */
  .post--teal { left: 822px; background: var(--deep-teal); color: var(--white); }
  .post--teal .quote { font-family: "Dancing Script", cursive; font-weight: 500; font-size: 21px; line-height: 27px; text-align: right; left: auto; right: 45px; width: auto; top: 72px; }
  .post--teal .author { font-family: "Caveat", cursive; font-weight: 700; font-size: 34px; text-align: right; left: auto; right: 46px; width: auto; top: 196px; }
  .post--teal .handle { top: 292px; }
</style>
</head>
<body>
<main class="post-row">

  <section class="post post--rose">
    <svg viewBox="0 0 314 314">
      <defs>
        <linearGradient id="rose-floral" x1="0" y1="0" x2="0" y2="1">
          <stop offset="0" stop-color="#ffffff" stop-opacity=".28"/>
          <stop offset="1" stop-color="#ffffff" stop-opacity=".12"/>
        </linearGradient>
      </defs>
      <polygon points="159,6 279,85 275,220 158,280 41,213 48,64" fill="none" stroke="var(--white)" stroke-width="1.6"/>
      <polygon points="172,14 287,98 268,230 146,286 38,200 58,58" fill="none" stroke="var(--white)" stroke-width="1.6"/>
      <rect x="22" y="32" width="46" height="230" rx="20" fill="url(#rose-floral)" role="img" aria-label="Hand-drawn leaf and flower sprays along the left side of the frame"/>
      <rect x="226" y="192" width="78" height="96" rx="24" fill="url(#rose-floral)" role="img" aria-label="Hand-drawn rose cluster at the lower right of the frame"/>
      <line x1="75" y1="198" x2="146" y2="198" stroke="var(--white)" stroke-width="1.4"/>
      <line x1="178" y1="198" x2="245" y2="198" stroke="var(--white)" stroke-width="1.4"/>
    </svg>
    <p class="post-text quote">Only those who dare<br><span class="small">– to fail greatly can –</span><br>Ever achieve greatly.</p>
    <p class="post-text closing-mark">”</p>
    <p class="post-text author">Walter J. Simmons</p>
    <p class="handle">@MorrowStudio</p>
  </section>

  <section class="post post--blush">
    <svg viewBox="0 0 314 314">
      <defs>
        <linearGradient id="blush-floral" x1="0" y1="0" x2="0" y2="1">
          <stop offset="0" stop-color="var(--faint-petal)" stop-opacity="0"/>
          <stop offset="1" stop-color="var(--faint-petal)" stop-opacity=".45"/>
        </linearGradient>
      </defs>
      <rect x="0" y="160" width="314" height="154" fill="url(#blush-floral)" role="img" aria-label="Faint outline peony flowers across the lower half of the card"/>
      <ellipse cx="154" cy="149" rx="140" ry="113" pathLength="100" fill="none" stroke="var(--ring)" stroke-width="5" stroke-linecap="round" stroke-dasharray="10 7 41 10 32"/>
    </svg>
    <span class="quote-mark quote-mark--open">“</span>
    <span class="quote-mark quote-mark--close">”</span>
    <p class="post-text headline">Don’t go<br>through life</p>
    <p class="post-text caps">GROW THROUGH<br>LIFE.</p>
    <p class="post-text author">Neil Ashcombe</p>
    <p class="handle">@MorrowStudio</p>
  </section>

  <section class="post post--teal">
    <svg viewBox="0 0 314 314">
      <defs>
        <linearGradient id="teal-floral" x1="0" y1="0" x2="1" y2="1">
          <stop offset="0" stop-color="#ffffff" stop-opacity=".22"/>
          <stop offset="1" stop-color="#ffffff" stop-opacity=".05"/>
        </linearGradient>
      </defs>
      <rect x="50" y="40" width="238" height="236" fill="var(--teal)"/>
      <polygon points="50,40 288,39 284,272 34,261" fill="none" stroke="var(--white)" stroke-width="1.6"/>
      <polygon points="48,52 290,54 286,276 50,276" fill="none" stroke="var(--white)" stroke-width="1.6"/>
      <path d="M28 24 H210 V62 H76 V210 H28 Z" fill="url(#teal-floral)" role="img" aria-label="Hand-drawn berry and leaf vines climbing the top-left corner of the frame"/>
    </svg>
    <p class="post-text quote">Follow your bliss and<br>the universe will open<br>doors where there<br>were only walls.</p>
    <p class="post-text author">Martin Oakley</p>
    <p class="handle">@MorrowStudio</p>
  </section>

</main>
</body>
</html>
```